Design a new jar label for a successful company

We are seeking a fresh label design that will be applied to a glass jar containing our high quality dried flower. We are a company based out of Washington State and we mainly sell dried herbs and oil extracts. The brand is "Copper Vale" and the product is "Copper Vale - Handcrafted Flower". I'd like to start with Black/Chrome as the color scheme, but we are open to other suggestions (for example dark purple instead of black). This will be professionally printed on a glossy label and the chrome or auxiliary colors can/will printed with a metallic foil.

BASIC REQUIREMENTS:

Size: 1.25" H x 2.5" L

Colors: Black and chrome. Preferably use a black background and make the logo/text chrome. Open to suggestions.

Margin: Please do not place any text within 1/16" around the edges to allow for deviation during die cutting process.

Logo: Use the Copper Vale shield as the center piece.

Required text: State "Handcrafted Flower" somewhere below the logo. Discretely place "TQDRN.COM" somewhere on the label.

Industry/Entity Type

Retail

Font styles to use
Other font styles liked:

Requirements
Must have
• The following warning most appear on the label. Please see attached graphic and also be sure to include the "21 and over" circular icon if possible:
• "Warning: This product has intoxicating effects and may be habit forming. Marijuana can impair concentration, coordination, and judgement. Do not operate a vehicle or machinery under the influence of this drug. There may be health risks associated with consumption of this product."
• "For use only by adults twenty-one and older. Keep out of reach of children."
• Note: You can use the circular 21 and over warning shown in the attached example instead of typing the text out.
Nice to have
• Fonts used - Doren Kessvik - FestivoLettersNo1.otf (This is the logo font.)
• Minion Pro - this is our standard copy font

```html
<!DOCTYPE html>
<html lang="en">
<head>
<meta charset="utf-8">
<title>Copper Vale – Handcrafted Flower Jar Label</title>
<link rel="stylesheet" href="https://fonts.googleapis.com/css2?family=Bebas+Neue&family=Oswald:wght@500;600&family=Barlow+Semi+Condensed:wght@600&family=Open+Sans:wght@600;700&display=swap">
<style>
  :root {
    --page: #ebebeb;
    --label-black: #000000;
    --violet: #8a1cf0;
    --violet-deep: #4a0a8c;
    --chrome: #ffffff;
  }
  * { box-sizing: border-box; margin: 0; padding: 0; }
  html, body {
    width: 1200px; height: 760px; overflow: hidden;
    background: var(--page);
  }
  .jar-label {
    position: absolute; left: 40px; top: 100px;
    width: 1120px; height: 560px;
    background: var(--label-black);
    overflow: hidden;
    color: var(--chrome);
  }
  .flower-art {
    position: absolute; left: 215px; top: 12px;
    width: 630px; height: 548px;
    background: radial-gradient(ellipse 48% 58% at 50% 52%, #7d18d8 0%, #4d0c90 38%, #1e0538 70%, rgba(0,0,0,0) 100%);
  }
  .age-badge {
    position: absolute; left: 45px; top: 42px;
    width: 150px; height: 150px;
  }
  .age-badge text { fill: var(--violet); font-family: "Open Sans", sans-serif; }
  .age-badge .ring-text { font-size: 15.5px; font-weight: 700; }
  .age-badge .age-number { font-size: 68px; font-weight: 700; letter-spacing: -3px; }
  .brand-title {
    position: absolute; left: 255px; width: 600px; text-align: center;
    font-family: "Bebas Neue", sans-serif; font-size: 150px; line-height: 1;
    color: var(--chrome); letter-spacing: 2px;
  }
  .brand-title.line-one { top: 210px; }
  .brand-title.line-two { top: 332px; }
  .product-line {
    position: absolute; left: 255px; width: 600px; top: 484px; text-align: center;
    font-family: "Oswald", sans-serif; font-weight: 600; font-size: 25px;
    letter-spacing: 5px; color: var(--chrome);
  }
  .site-url {
    position: absolute; left: 49px; top: 444px;
    font-family: "Bebas Neue", sans-serif; font-size: 42px; letter-spacing: 1px;
  }
  .social-handle {
    position: absolute; left: 50px; top: 494px;
    display: flex; align-items: center; gap: 10px;
    font-family: "Barlow Semi Condensed", sans-serif; font-weight: 600; font-size: 23px;
  }
  .social-handle .dot {
    width: 22px; height: 22px; border: 2.5px solid var(--chrome); border-radius: 50%;
  }
  .warning-panel {
    position: absolute; left: 869px; top: 72px; width: 230px;
    text-align: center; font-family: "Oswald", sans-serif; text-transform: uppercase;
  }
  .warning-title {
    color: var(--violet); font-weight: 600; font-size: 28px; letter-spacing: 3px; line-height: 1;
  }
  .warning-copy {
    margin-top: 14px; font-weight: 500; font-size: 16px; line-height: 22.4px; letter-spacing: 1px;
  }
  .child-notice {
    margin-top: 22px; color: var(--violet); font-weight: 600; font-size: 16.5px;
    line-height: 22.4px; letter-spacing: 1px;
  }
</style>
</head>
<body>
  <main class="jar-label">
    <div class="flower-art" role="img" aria-label="Purple-toned cannabis flower with a snowy mountain peak and stars at its top"></div>

    <svg class="age-badge" viewBox="0 0 150 150" aria-label="For use only by adults 21 or older">
      <defs>
        <path id="badge-ring" d="M75,75 m-58,0 a58,58 0 1,1 116,0 a58,58 0 1,1 -116,0"/>
      </defs>
      <text class="ring-text"><textPath href="#badge-ring" startOffset="12" textLength="345" lengthAdjust="spacing">FOR USE ONLY BY ADULTS 21 OR OLDER.</textPath></text>
      <text class="age-number" x="73" y="99" text-anchor="middle">21</text>
    </svg>

    <h1 class="brand-title line-one">COPPER</h1>
    <div class="brand-title line-two">VALE</div>
    <p class="product-line">HANDCRAFTED FLOWER</p>

    <p class="site-url">TQDRN.COM</p>
    <p class="social-handle"><span class="dot"></span>@mycoppervale</p>

    <section class="warning-panel">
      <h2 class="warning-title">WARNING:</h2>
      <p class="warning-copy">
        This product has<br>intoxicating effects and<br>may be habit forming.<br>Marijuana can impair<br>concentration,<br>coordination, and<br>judgement.<br>Do not operate a vehicle or<br>machinery under the<br>influence of this drug.<br>There may be health risks<br>associated with<br>consumption<br>of this product.
      </p>
      <p class="child-notice">Keep out of reach of<br>children.</p>
    </section>
  </main>
</body>
</html>
```